Talents and colours poster for home office

The objective is to illustrate/communicate and remember 5 talents and 4 colours of the personality.

The infographic will be hanged on the wall of an home office. It need to be simple and clear. Illustrations and pictograms can be used. It can be artistic.

Here's the content:

5 talents,scaling in priority from #1 to #5
Ideation / creativity
Winning other over / charisma
Adaptability
Positivity
Empathy

In the files there is a description of what those mean.

You have to include 4 colours, scaling in priority from #1 to #4
Yellow
Green
Red
Blue

I made a sketch just for fun... and to show why I need professionnal skills :)

THX

Office

• offensive materials

```html
<!DOCTYPE html>
<html lang="en">
<head>
<meta charset="UTF-8">
<title>Talents Poster</title>
<link rel="stylesheet" href="https://fonts.googleapis.com/css2?family=Oswald:wght@500&display=swap">
<style>
  :root {
    --frame-dark: #3d2412;
    --frame-gold: #e2aa22;
    --frame-light: #f7d45a;
    --mat-grey: #5a5856;
    --panel-brown: #3e2216;
    --rule-gold: #e9c585;
    --ornament-gold: #c8962c;
    --yellow-a: #e9d41c;
    --yellow-b: #f7ef45;
    --green-a: #a9d25c;
    --green-b: #7cb63a;
    --red-a: #e1312a;
    --red-b: #e84036;
    --blue-dark-a: #2b4a80;
    --blue-dark-b: #3e5f99;
    --blue-light-a: #5a82c2;
    --blue-light-b: #6d94cf;
    --label-white: #ffffff;
  }
  html, body {
    margin: 0;
    padding: 0;
    overflow: hidden;
  }
  .poster {
    position: relative;
    width: 1068px;
    height: 1200px;
    overflow: hidden;
    background: var(--frame-dark);
    font-family: "Oswald", "Arial Narrow", sans-serif;
  }
  .frame {
    position: absolute;
    inset: 0;
    background:
      linear-gradient(90deg, var(--frame-gold) 0%, var(--frame-light) 8%, var(--frame-gold) 15%, transparent 15%, transparent 85%, var(--frame-gold) 85%, var(--frame-light) 92%, var(--frame-gold) 100%),
      linear-gradient(180deg, var(--frame-gold) 0%, var(--frame-light) 7%, var(--frame-gold) 14%, var(--frame-dark) 14%, var(--frame-dark) 86%, var(--frame-gold) 86%, var(--frame-light) 93%, var(--frame-gold) 100%);
  }
  .mat {
    position: absolute;
    left: 193px;
    top: 187px;
    width: 696px;
    height: 816px;
    background: var(--mat-grey);
    box-shadow: 0 0 0 14px var(--frame-dark), 0 0 0 20px var(--frame-gold);
  }
  .panel {
    position: absolute;
    left: 220px;
    top: 209px;
    width: 644px;
    height: 774px;
    background: var(--panel-brown);
  }
  .flourish {
    position: absolute;
    left: 320px;
    width: 447px;
    height: 71px;
    background: linear-gradient(90deg, transparent, var(--ornament-gold) 20%, var(--ornament-gold) 80%, transparent);
    opacity: 0.55;
  }
  .flourish--top { top: 229px; }
  .flourish--bottom { top: 891px; }
  .rule {
    position: absolute;
    left: 257px;
    width: 570px;
    height: 3px;
    background: var(--rule-gold);
  }
  .talent {
    position: absolute;
    left: 257px;
    width: 570px;
    height: 80px;
    display: flex;
    align-items: center;
    justify-content: center;
    color: var(--label-white);
    font-size: 28px;
    font-weight: 500;
    letter-spacing: 0.2px;
    text-transform: uppercase;
    text-shadow: 1px 1px 1px rgba(0,0,0,0.55);
    margin: 0;
  }
  .talent--ideation   { top: 324px; background: linear-gradient(90deg, var(--yellow-a), var(--yellow-b) 50%, var(--yellow-a)); }
  .talent--charisma   { top: 440px; background: linear-gradient(90deg, var(--green-a), var(--green-b)); }
  .talent--adapt      { top: 557px; background: linear-gradient(90deg, var(--red-a), var(--red-b)); }
  .talent--positivity { top: 675px; background: linear-gradient(180deg, var(--blue-dark-b), var(--blue-dark-a)); }
  .talent--empathy    { top: 792px; background: linear-gradient(180deg, var(--blue-light-b), var(--blue-light-a)); }
</style>
</head>
<body>
<div class="poster">
  <div class="frame" role="img" aria-label="Ornate carved gold picture frame with scrolled corner ornaments"></div>
  <div class="mat"></div>
  <div class="panel"></div>
  <div class="flourish flourish--top" role="img" aria-label="Gold scrollwork flourish"></div>
  <div class="flourish flourish--bottom" role="img" aria-label="Gold scrollwork flourish"></div>

  <div class="rule" style="top:304px"></div>
  <p class="talent talent--ideation">Ideation / Creativity</p>
  <div class="rule" style="top:421px"></div>
  <p class="talent talent--charisma">Winning Other Over / Charisma</p>
  <div class="rule" style="top:537px"></div>
  <p class="talent talent--adapt">Adaptability</p>
  <div class="rule" style="top:655px"></div>
  <p class="talent talent--positivity">Positivity</p>
  <div class="rule" style="top:772px"></div>
  <p class="talent talent--empathy">Empathy</p>
  <div class="rule" style="top:888px"></div>
</div>
</body>
</html>
```